Brightfernrx website

We are a weight loss clinic and we need a website built. please look at these websites for content and style. Just need like 5 pages see samples. AI files of logo are not avail yet so use sample for place set

https://glowshiftstudio.com/
ortanvital.com
https://pinecrestclinicalbodybalance.com/
https://yourslimmingnook.com/
https://qrvskinstudio.com/treatments/weight-loss-injections/

Target Market(s)

Women

Industry/Entity Type

weight loss

Coding

Coded - Design and coding required

Number of Pages Required

5+ page

Requirements
Nice to have
• please make look like a medspa website

```html
<!DOCTYPE html>
<html lang="en">
<head>
<meta charset="utf-8">
<title>Brightfernrx — Wellness and Weight Loss Experts</title>
<link href="https://fonts.googleapis.com/css2?family=Cinzel:wght@400;600&family=Rubik:wght@400;500;700&display=swap" rel="stylesheet">
<style>
:root{
  --green:#8cc63f;
  --green-dark:#6fa52a;
  --blue:#1e96d6;
  --blue-dark:#1678b3;
  --ink:#2e2e2e;
  --muted:#6b6b6b;
  --line:#e3e3e3;
  --white:#ffffff;
}
*{margin:0;padding:0;box-sizing:border-box}
html,body{width:1200px;height:4416px;overflow:hidden}
body{font-family:"Rubik",Arial,sans-serif;color:var(--ink);background:var(--white);position:relative}
.abs{position:absolute}
.photo{position:absolute}
.btn{display:inline-block;font-size:13px;font-weight:500;letter-spacing:1px;text-transform:uppercase;padding:12px 30px;border-radius:4px}
.btn-outline-white{border:2px solid var(--white);color:var(--white)}
.btn-outline-blue{border:2px solid var(--blue);color:var(--blue)}
.btn-green{background:var(--green);color:var(--white)}
.btn-blue{background:var(--blue);color:var(--white)}
.eyebrow{font-size:14px;letter-spacing:3px;text-transform:uppercase}
p.body{font-size:15px;line-height:1.65;color:var(--muted)}
.rule{display:block;width:110px;height:2px}

/* header */
.site-header{top:0;left:0;width:1200px;height:100px;background:var(--white)}
.brand{left:60px;top:28px;display:flex;align-items:center;gap:12px}
.brand-mark{width:36px;height:36px;border-radius:50%;background:var(--green)}
.brand-name{font-weight:700;font-size:28px;color:var(--blue)}
.main-nav{left:410px;top:58px;display:flex;gap:30px;font-size:14px;font-weight:500;text-transform:uppercase}
.main-nav a{color:var(--ink)}
.main-nav a.active{color:var(--green)}
.topbar{right:0;top:0;height:40px;display:flex}
.topbar .call{background:var(--blue);color:var(--white);font-size:13px;padding:12px 22px;display:flex;gap:8px;align-items:center}
.topbar .book{background:var(--green);color:var(--white);font-size:13px;font-weight:500;padding:12px 22px}

/* hero */
.hero{top:100px;left:0;width:1200px;height:640px;background:linear-gradient(120deg,#7cbf3a 0%,#9fd14f 55%,#b7dd6e 100%);overflow:hidden}
.hero-blue{right:0;top:0;width:120px;height:640px;background:linear-gradient(180deg,#2aa3e0,#1a8fd0)}
.hero-photo{left:660px;top:0;width:440px;height:640px;background:linear-gradient(180deg,#e9c9a8 0%,#f0d24a 40%,#e7c032 75%,#d8c25a 100%)}
.hero-text{left:120px;top:160px;color:var(--white)}
.hero-text .eyebrow{font-size:16px}
.hero-text h1{font-family:"Cinzel",serif;font-weight:400;font-size:52px;line-height:1.12;margin:18px 0 30px;width:520px}

.feature-cards{top:660px;left:120px;display:flex;gap:24px}
.feature-card{width:300px;height:180px;background:var(--white);border-radius:8px;box-shadow:0 8px 24px rgba(0,0,0,.12);padding:26px;border-bottom:4px solid var(--green)}
.feature-card svg{display:block;margin-bottom:12px}
.feature-card h3{font-size:15px;font-weight:700;color:var(--green);text-transform:uppercase;margin-bottom:8px}
.feature-card p{font-size:13px;line-height:1.5;color:var(--muted)}

/* about */
.about-collage-a{left:110px;top:940px;width:250px;height:260px;background:linear-gradient(160deg,#f1ece6 0%,#dcc4ae 55%,#b99a80 100%)}
.about-collage-b{left:300px;top:1080px;width:270px;height:290px;background:linear-gradient(160deg,#dfe7ef 0%,#e8d2b8 45%,#e2cf52 100%);border:6px solid var(--white);box-shadow:0 6px 20px rgba(0,0,0,.12)}
.about-frame{left:90px;top:1180px;width:110px;height:160px;border-left:3px solid var(--green);border-bottom:3px solid var(--green)}
.about-text{left:640px;top:960px;width:470px}
.about-text .eyebrow{color:var(--green)}
.about-text h2{font-family:"Cinzel",serif;font-weight:400;font-size:40px;color:var(--blue);margin:10px 0 20px}
.about-text p{margin-bottom:16px}

/* program */
.program{top:1480px;left:0;width:1200px;height:580px;background:linear-gradient(120deg,#1a8fd0,#2aa3e0)}
.program-text{left:120px;top:150px;width:460px;color:var(--white)}
.program-text h2{font-family:"Cinzel",serif;font-weight:400;font-size:38px;line-height:1.15;margin:10px 0 20px}
.program-text p{font-size:15px;line-height:1.65;color:#e8f4fb;margin-bottom:26px}
.program-ring{left:660px;top:60px;width:460px;height:460px;border-radius:50%;border:10px solid var(--white)}
.program-photo{left:680px;top:80px;width:420px;height:420px;border-radius:50%;background:linear-gradient(160deg,#f0dccb 0%,#8fc84a 35%,#6fae2c 70%,#3b3f45 100%)}

/* services */
.service-card{top:2150px;width:480px}
.service-photo{width:480px;height:300px}
.service-body{position:relative;margin:-70px 0 0 30px;width:430px;background:var(--white);box-shadow:0 8px 24px rgba(0,0,0,.12);padding:28px 30px;border-radius:4px}
.service-body h3{font-family:"Cinzel",serif;font-weight:400;font-size:28px;margin-bottom:12px}
.service-body p{font-size:14px;line-height:1.6;color:var(--muted);margin-bottom:18px}

/* success */
.success{top:2620px;left:0;width:1200px;height:420px;background:linear-gradient(120deg,#7cbf3a,#9fd14f)}
.success-head{top:2690px;left:0;width:1200px;text-align:center;color:var(--white)}
.success-head h2{font-family:"Cinzel",serif;font-weight:400;font-size:40px;margin-top:10px}
.success-head .rule{margin:16px auto 0;background:var(--white)}
.gallery{top:2940px;left:130px;display:flex;gap:8px;align-items:flex-end}
.gallery-item{width:110px;height:200px}
.gallery-feature{width:180px;height:240px}
.gallery-labels{top:3180px;left:430px;width:340px;display:flex}
.gallery-labels span{flex:1;background:var(--blue);color:var(--white);text-align:center;font-size:15px;letter-spacing:2px;padding:12px 0}
.gallery-labels span + span{background:var(--blue-dark)}

/* blogs */
.blogs-title{top:3290px;left:110px;font-family:"Cinzel",serif;font-weight:400;font-size:40px;color:var(--green)}
.blogs-rule{top:3350px;left:110px;background:var(--green)}
.blog-feature{top:3400px;left:110px;width:500px;height:400px;background:linear-gradient(160deg,#e8f0f4 0%,#ecd9c6 40%,#c7a07a 100%)}
.blog-feature-caption{top:3680px;left:140px;width:420px;color:var(--white)}
.date-tag{display:inline-block;background:var(--green);color:var(--white);font-size:12px;padding:5px 10px;margin-bottom:8px}
.blog-feature-caption h3{font-size:20px;font-weight:500;line-height:1.35}
.blog-small-photo{left:630px;width:220px;height:190px}
.blog-small-card{left:840px;width:250px;height:170px;background:var(--white);box-shadow:0 6px 20px rgba(0,0,0,.1);padding:18px 20px}
.blog-small-card h4{font-size:15px;font-weight:700;margin-bottom:6px}
.blog-small-card p{font-size:12px;line-height:1.5;color:var(--muted);margin-bottom:8px}
.blog-small-card .more{font-size:11px;color:var(--green);font-weight:700;text-transform:uppercase}

/* cta */
.cta{top:3910px;left:0;width:1200px;height:130px;background:linear-gradient(90deg,#1a8fd0,#2aa3e0)}
.cta-text{left:110px;top:50px;color:var(--white);font-size:26px;font-weight:700;text-transform:uppercase}
.cta-book{right:0;top:0;width:380px;height:130px;background:var(--green);clip-path:polygon(12% 0,100% 0,100% 100%,0 100%);color:var(--white);font-size:20px;font-weight:700;text-transform:uppercase;display:flex;align-items:center;justify-content:center;padding-left:40px}

/* footer */
.footer-brand{left:110px;top:4110px;display:flex;align-items:center;gap:12px}
.socials{left:110px;top:4200px;display:flex;gap:10px}
.socials span{width:30px;height:30px;border-radius:50%;background:var(--green)}
.footer-col{top:4110px}
.footer-col h5{font-size:15px;font-weight:700;text-transform:uppercase;color:var(--ink);padding-bottom:8px;border-bottom:2px solid var(--green);display:inline-block;margin-bottom:12px}
.footer-col li{list-style:none;font-size:13px;color:var(--muted);line-height:1.9;display:flex;gap:8px;align-items:center}
.copyright{top:4340px;left:0;width:1200px;height:76px;border-top:1px solid var(--line);text-align:center;font-size:12px;color:var(--muted);padding-top:30px}
</style>
</head>
<body>

<header class="abs site-header">
  <div class="abs brand"><span class="brand-mark"></span><span class="brand-name">Brightfernrx</span></div>
  <nav class="abs main-nav">
    <a class="active">Home</a><a>About Us</a><a>Services</a><a>Why Us</a><a>Before &amp; After</a><a>Blogs</a><a>Contact Us</a>
  </nav>
  <div class="abs topbar">
    <div class="call">
      <svg width="14" height="14" viewBox="0 0 24 24"><path fill="#fff" d="M6.6 10.8a15 15 0 006.6 6.6l2.2-2.2a1 1 0 011-.25 11 11 0 003.5.56 1 1 0 011 1V20a1 1 0 01-1 1A17 17 0 013 4a1 1 0 011-1h3.5a1 1 0 011 1 11 11 0 00.56 3.5 1 1 0 01-.25 1z"/></svg>
      Call us (555) 014 2290
    </div>
    <div class="book">BOOK CONSULTATION →</div>
  </div>
</header>

<section class="abs hero">
  <div class="abs hero-blue"></div>
  <div class="photo hero-photo" role="img" aria-label="Smiling fit woman in yellow activewear holding a measuring tape"></div>
  <div class="abs hero-text">
    <div class="eyebrow">Welcome to Brightfernrx</div>
    <h1>Wellness and Weight Loss Experts</h1>
    <span class="btn btn-outline-white">Learn More</span>
  </div>
</section>

<div class="abs feature-cards">
  <div class="feature-card">
    <svg width="34" height="34" viewBox="0 0 34 34"><rect x="4" y="6" width="26" height="22" rx="4" fill="none" stroke="#8cc63f" stroke-width="2.5"/><circle cx="17" cy="17" r="5" fill="none" stroke="#8cc63f" stroke-width="2.5"/></svg>
    <h3>Weight Loss</h3>
    <p>Lorem ipsum dolor sit amet, consectetur adipiscing elit, sed do eiusmod.</p>
  </div>
  <div class="feature-card">
    <svg width="34" height="34" viewBox="0 0 34 34"><path d="M17 29C8 22 4 16 8 10c3-4 7-3 9 1 2-4 6-5 9-1 4 6 0 12-9 19z" fill="none" stroke="#8cc63f" stroke-width="2.5"/></svg>
    <h3>Wellness Service</h3>
    <p>Lorem ipsum dolor sit amet, consectetur adipiscing elit, sed do eiusmod.</p>
  </div>
  <div class="feature-card">
    <svg width="34" height="34" viewBox="0 0 34 34"><circle cx="17" cy="17" r="12" fill="none" stroke="#8cc63f" stroke-width="2.5"/><path d="M11 18l4 4 8-9" fill="none" stroke="#8cc63f" stroke-width="2.5"/></svg>
    <h3>Rejuvenation</h3>
    <p>Lorem ipsum dolor sit amet, consectetur adipiscing elit, sed do eiusmod.</p>
  </div>
</div>

<section>
  <div class="abs about-frame"></div>
  <div class="photo about-collage-a" role="img" aria-label="Woman measuring her waist with a tape"></div>
  <div class="photo about-collage-b" role="img" aria-label="Group of women exercising together outdoors"></div>
  <div class="abs about-text">
    <div class="eyebrow">Who we are</div>
    <h2>About Brightfernrx</h2>
    <p class="body">Lorem ipsum dolor sit amet, consectetur adipiscing elit, sed do eiusmod tempor incididunt ut labore et dolore magna aliqua. Ut enim ad minim veniam, quis nostrud exercitation ullamco laboris nisi ut aliquip ex ea commodo consequat.</p>
    <p class="body">Duis aute irure dolor in reprehenderit in voluptate velit esse cillum dolore eu fugiat nulla pariatur. Excepteur sint occaecat cupidatat non proident, sunt in culpa qui officia.</p>
    <span class="btn btn-outline-blue" style="margin-top:10px">Learn More</span>
  </div>
</section>

<section class="abs program">
  <div class="abs program-text">
    <div class="eyebrow">Medically Supervised</div>
    <h2>Weight Loss Program</h2>
    <p>Lorem ipsum dolor sit amet, consectetur adipiscing elit, sed do eiusmod tempor incididunt ut labore et dolore magna aliqua. Ut enim ad minim veniam, quis nostrud exercitation ullamco laboris nisi ut aliquip ex ea commodo consequat. Duis aute irure dolor in reprehenderit.</p>
    <span class="btn btn-green">Learn More</span>
  </div>
  <div class="abs program-ring"></div>
  <div class="photo program-photo" role="img" aria-label="Athletic woman doing a plank exercise on a green mat"></div>
</section>

<article class="abs service-card" style="left:110px">
  <div class="service-photo" role="img" aria-label="Woman relaxing during a spa massage" style="background:linear-gradient(150deg,#8a6a52 0%,#c9a98c 45%,#efe4da 100%)"></div>
  <div class="service-body">
    <h3 style="color:var(--green)">Wellness Service</h3>
    <p>Lorem ipsum dolor sit amet, consectetur adipiscing elit, sed do eiusmod tempor incididunt ut labore et dolore.</p>
    <span class="btn btn-green" style="padding:9px 24px;font-size:12px">Learn More</span>
  </div>
</article>
<article class="abs service-card" style="left:610px">
  <div class="service-photo" role="img" aria-label="Woman receiving a facial rejuvenation treatment" style="background:linear-gradient(150deg,#f5f6f7 0%,#e8d9cc 50%,#cdd4d9 100%)"></div>
  <div class="service-body">
    <h3 style="color:var(--blue)">Rejuvenation</h3>
    <p>Lorem ipsum dolor sit amet, consectetur adipiscing elit, sed do eiusmod tempor incididunt ut labore et dolore.</p>
    <span class="btn btn-blue" style="padding:9px 24px;font-size:12px">Learn More</span>
  </div>
</article>

<section class="abs success"></section>
<div class="abs success-head">
  <div class="eyebrow">Before &amp; After Gallery</div>
  <h2>Real Success Stories</h2>
  <span class="rule"></span>
</div>
<div class="abs gallery">
  <div class="gallery-item" role="img" aria-label="Before photo, woman in red activewear" style="background:linear-gradient(#e9e6e2 0%,#d8b39a 35%,#c9452f 70%,#3a3a3a 100%)"></div>
  <div class="gallery-item" role="img" aria-label="After photo, woman in yellow activewear" style="background:linear-gradient(#e9e6e2 0%,#d8b39a 35%,#d6d84a 70%,#3a3a3a 100%)"></div>
  <div class="gallery-item" role="img" aria-label="Before photo, woman in sports top" style="background:linear-gradient(#e9e6e2 0%,#c99a7c 40%,#2f2f2f 100%)"></div>
  <div class="gallery-feature" role="img" aria-label="Before photo, woman in black sportswear" style="background:linear-gradient(#eef0f1 0%,#dcb89e 40%,#2b2b2b 70%,#d5b196 100%)"></div>
  <div class="gallery-feature" role="img" aria-label="After photo, slimmer woman in black sportswear" style="background:linear-gradient(#eef0f1 0%,#dcb89e 40%,#2b2b2b 65%,#d5b196 100%)"></div>
  <div class="gallery-item" role="img" aria-label="Before photo, man in shorts" style="background:linear-gradient(#e9e6e2 0%,#b07a58 40%,#4a5a75 100%)"></div>
  <div class="gallery-item" role="img" aria-label="After photo, man in shorts" style="background:linear-gradient(#e9e6e2 0%,#7a5038 40%,#3a4a65 100%)"></div>
</div>
<div class="abs gallery-labels"><span>BEFORE</span><span>AFTER</span></div>

<h2 class="abs blogs-title">Latest Blogs</h2>
<span class="abs rule blogs-rule"></span>
<div class="photo blog-feature" role="img" aria-label="Slim waist with measuring tape"></div>
<div class="abs blog-feature-caption">
  <span class="date-tag">05 DEC 2023</span>
  <h3>Lorem ipsum dolor sit amet, consectetur adipiscing elit, sed do eiusmod tempor</h3>
</div>
<div class="photo blog-small-photo" role="img" aria-label="Woman doing lunges" style="top:3400px;background:linear-gradient(135deg,#e6e7e8 0%,#9ea2a8 60%,#3a3c40 100%)"></div>
<div class="abs blog-small-card" style="top:3420px">
  <span class="date-tag">05 DEC 2023</span>
  <h4>Lorem ipsum dolor sit</h4>
  <p>Duis aute irure dolor in reprehenderit in voluptate velit esse.</p>
  <span class="more">Learn More</span>
</div>
<div class="photo blog-small-photo" role="img" aria-label="Healthy food with fitness gear" style="top:3610px;background:linear-gradient(135deg,#f2f2f0 0%,#9fc96a 45%,#e07a3a 100%)"></div>
<div class="abs blog-small-card" style="top:3630px">
  <span class="date-tag">05 DEC 2023</span>
  <h4>Lorem ipsum dolor sit</h4>
  <p>Duis aute irure dolor in reprehenderit in voluptate velit esse.</p>
  <span class="more">Learn More</span>
</div>

<section class="abs cta">
  <div class="abs cta-text">Call and schedule your appointment today!</div>
  <div class="abs cta-book">Book Appointment →</div>
</section>

<footer>
  <div class="abs footer-brand"><span class="brand-mark"></span><span class="brand-name">Brightfernrx</span></div>
  <div class="abs socials"><span></span><span></span><span></span><span></span><span></span></div>
  <div class="abs footer-col" style="left:470px">
    <h5>Company</h5>
    <ul><li>About Us</li><li>Services</li><li>Why Us</li><li>Contact Us</li></ul>
  </div>
  <div class="abs footer-col" style="left:650px">
    <h5>Hours</h5>
    <ul><li>Working Hours</li><li>Mon, Tue, Thu &amp; Fri 9am-5pm</li><li>Sat 9am-1pm</li></ul>
  </div>
  <div class="abs footer-col" style="left:880px">
    <h5>Contact Us</h5>
    <ul>
      <li><svg width="12" height="14" viewBox="0 0 12 14"><path d="M6 0a5 5 0 015 5c0 4-5 9-5 9S1 9 1 5a5 5 0 015-5z" fill="#8cc63f"/><circle cx="6" cy="5" r="2" fill="#fff"/></svg>418 Fernhollow Way Ste 12<br>Cedar Vale, TX 70412</li>
      <li><svg width="12" height="12" viewBox="0 0 24 24"><path fill="#8cc63f" d="M6.6 10.8a15 15 0 006.6 6.6l2.2-2.2a1 1 0 011-.25 11 11 0 003.5.56 1 1 0 011 1V20a1 1 0 01-1 1A17 17 0 013 4a1 1 0 011-1h3.5a1 1 0 011 1 11 11 0 00.56 3.5 1 1 0 01-.25 1z"/></svg>(555) 014 2290</li>
      <li><svg width="12" height="10" viewBox="0 0 12 10"><rect x=".5" y=".5" width="11" height="9" fill="none" stroke="#8cc63f"/><path d="M.5.5L6 5l5.5-4.5" fill="none" stroke="#8cc63f"/></svg>info@brightfernrx.com</li>
    </ul>
  </div>
  <div class="abs copyright">Copyright © 2023 BRIGHTFERNRX. All Rights Reserved</div>
</footer>

</body>
</html>
```